Indian Takeaway Menu -

I would like to have double parallel fold A4 sheet menu.
A4 sheet cut in half and attached to the other half to make the sheet 4 small pages long.

Colors
abd036
ffffff

Requirements
Must have
• Please check new attachments - menu size and layout is not correct.
• I would like to add Dark brown colour. A4 sheet folded 4x Menu layout pocket size.
Nice to have
• Dark Brown - Parrot Green and very light Brown

```html
<!DOCTYPE html>
<html lang="en">
<head>
<meta charset="utf-8">
<title>Indian Takeaway Menu</title>
<link href="https://fonts.googleapis.com/css2?family=Mountains+of+Christmas:wght@700&family=Arimo:ital,wght@0,400;0,700;1,400&display=swap" rel="stylesheet">
<style>
  :root{
    --parrot:#abd036;
    --white:#ffffff;
    --brown:#3b2414;
    --brown-soft:#5a3a22;
    --red:#c6302a;
    --tile-1:#8a5a2b;
    --tile-2:#c2702a;
    --tile-3:#d9b776;
  }
  *{box-sizing:border-box;margin:0;padding:0}
  html,body{width:1200px;height:848px;overflow:hidden;background:var(--parrot)}
  .menu{position:relative;width:1200px;height:848px;background:var(--parrot);color:var(--brown);font-family:"Arimo",Arial,sans-serif;font-size:12.6px;line-height:16px}
  .col{position:absolute;top:0;height:848px}
  .col-1{left:8px;width:284px}
  .col-2{left:312px;width:286px}
  .col-3{left:608px;width:288px}
  .col-4{left:910px;width:282px}
  .block{position:absolute;left:0;right:0}
  .section-title{position:absolute;height:38px;background:var(--red);color:var(--white);font-family:"Mountains of Christmas",cursive;font-weight:700;font-size:24px;line-height:38px;padding-left:10px;white-space:nowrap}
  .col-1 .section-title{left:-8px;width:300px}
  .col-2 .section-title{left:-8px;width:295px}
  .col-3 .section-title{left:-8px;width:296px}
  .col-4 .section-title{left:-8px;width:300px}
  .item{margin-bottom:7px}
  .item-line{display:flex;align-items:baseline;gap:4px}
  .name{font-family:"Mountains of Christmas",cursive;font-weight:700;font-size:15px;color:var(--brown);text-decoration:underline;text-decoration-thickness:1px;text-underline-offset:2px;white-space:nowrap}
  .codes{font-size:12px;white-space:nowrap}
  .leader{flex:1;border-bottom:2px dotted var(--brown);min-width:10px;transform:translateY(-3px)}
  .price{font-weight:700;font-size:13.5px;white-space:nowrap}
  .desc{font-size:12.6px;line-height:16px}
  .veg{display:inline-block;width:13px;height:13px;border-radius:50%;background:var(--red);color:var(--white);font-size:9px;font-weight:700;line-height:13px;text-align:center;transform:translateY(-1px)}
  .veg.mild{background:#e8a62a}
  .note{color:var(--red);font-style:italic;font-weight:700;font-size:12.6px}
  .side-list{list-style:none}
  .side-list li{display:flex;align-items:baseline;gap:4px;height:16px}
  .side-list .name{font-size:14.5px;text-decoration:none}
  .photos{position:absolute;left:0;top:643px;display:grid;grid-template-columns:repeat(3,88px);grid-auto-rows:88px;gap:7px}
  .photo{border:3px solid var(--white);box-shadow:0 1px 3px rgba(0,0,0,.3)}
  .photo svg{display:block;width:100%;height:100%}
</style>
</head>
<body>
<main class="menu">

  <section class="col col-1">
    <div class="block" style="top:2px">
      <div class="item">
        <p class="item-line"><span class="name">Chicken Tikka Kebab</span><span class="codes">2,3,6</span><span class="leader"></span><span class="price">8.00</span></p>
        <p class="desc">Chicken breast marinated in spices, barbecued served with garlic mayo, chilli sauce &amp; mixed salad &amp; wrapped in naan.</p>
      </div>
      <div class="item">
        <p class="item-line"><span class="name">Mix Kebab</span><span class="codes">2,3,6</span><span class="leader"></span><span class="price">8.00</span></p>
        <p class="desc">Pieces of chicken tikka &amp; donner meat with garlic mayo, sweet chilli &amp; salad wrapped in naan bread.</p>
      </div>
      <div class="item">
        <p class="item-line"><span class="name">Garlic Chips</span><span class="leader"></span><span class="price">4.00</span></p>
      </div>
    </div>

    <h2 class="section-title" style="top:188px">Chef Arora's Special Curries</h2>
    <div class="block" style="top:232px">
      <div class="item">
        <p class="item-line"><span class="name">Butter Murgh</span><span class="codes">3,5</span><span class="leader"></span><span class="price">10.50</span></p>
        <p class="desc">Chicken cooked in tandoor mixed with rich Tomato creamy cashew sauce, splash of cream with hint of honey &amp; dry fenugreek.</p>
      </div>
      <div class="item">
        <p class="item-line"><span class="name">Laal Maas</span><span class="leader"></span><span class="price">11.50</span></p>
        <p class="desc">Taditional rajasthani lamb cooked with garlic and ginger , degi chilli powder, tomatoes finished with star aniseed and clove powder.</p>
      </div>
      <div class="item">
        <p class="item-line"><span class="name">Shahi Veg Kofta</span><span class="codes">3,5</span><span class="leader"></span><span class="price">10.00</span></p>
        <p class="desc">Handmade veg and panner dumplings simmered in tomato sauce, musky fenugreek sauce finished with touch of honey and cream.</p>
      </div>
      <div class="item">
        <p class="item-line"><span class="name">Kerala Prawn</span><span class="codes">14</span><span class="leader"></span><span class="price">12.00</span></p>
        <p class="desc">Delicacy of kerala spices, tomato and red onion gravy finished with touch of fresh coconut milk.</p>
      </div>
    </div>

    <h2 class="section-title" style="top:596px">Chicken Dishes</h2>
    <div class="block" style="top:648px">
      <div class="item" style="margin-bottom:18px">
        <p class="item-line"><span class="name">Punjabi Saag</span><span class="codes">3</span><span class="veg">V</span><span class="leader"></span><span class="price">9.95</span></p>
        <p class="desc">Chicken cooked with spinach, ginger, garlic, fresh cream &amp; temperd with Punjabi tarka.</p>
      </div>
      <div class="item">
        <p class="item-line"><span class="name">Royale Korma</span><span class="codes">3, 5</span><span class="leader"></span><span class="price">8.95</span></p>
        <p class="desc">Breast of chicken cooked in a rich creamy sauce with saffron &amp; coconut , probably most popular among Irish.</p>
      </div>
    </div>
  </section>

  <section class="col col-2">
    <div class="block" style="top:2px">
      <div class="item">
        <p class="item-line"><span class="name">Saffron House Chicken Curry</span><span class="codes">3,4,5</span></p>
        <p class="item-line"><span class="leader"></span><span class="price">8.95</span></p>
        <p class="desc">Traditional curry cooked with coconut ,mustard seed , cashews and curry leaves.</p>
      </div>
      <div class="item">
        <p class="item-line"><span class="name">Chicken Karahi</span><span class="leader"></span><span class="price">8.95</span></p>
        <p class="desc">Boneless chicken Prepared in Deg with peppers,onion, tomatoes and Indian whole spices.</p>
      </div>
      <div class="item">
        <p class="item-line"><span class="name">Chicken Tikka Masala</span><span class="codes">3</span><span class="leader"></span><span class="price">8.95</span></p>
        <p class="desc">Chicken roasted in clayoven and simmered in smooth creamy tomato sauce with palm crushed fenugreek leaves and jiggery .</p>
      </div>
      <div class="item">
        <p class="item-line"><span class="name">South Indian Garlic Chilli</span><span class="leader"></span><span class="price">8.95</span></p>
        <p class="desc">Chicken cooked in South Indian style and loaded with garlic, ground spices, fresh herbs.</p>
      </div>
      <div class="item">
        <p class="item-line"><span class="name">Chicken Daiwala</span><span class="codes">3</span><span class="leader"></span><span class="price">8.95</span></p>
        <p class="desc">Amazingly spicy chicken curry cooked with yogurt, green chillies, ginger and herbs.</p>
      </div>
      <div class="item">
        <p class="item-line"><span class="name">Murgh Biryani</span><span class="codes">3,5</span><span class="veg">V</span><span class="leader"></span><span class="price">9.95</span></p>
        <p class="desc">Perfumed basmati rice with chicken cubes, nuts , golden onions and biryani spices , served with sauce.</p>
      </div>
    </div>

    <h2 class="section-title" style="top:484px">Lamb Dishes</h2>
    <div class="block" style="top:532px">
      <div class="item">
        <p class="item-line"><span class="name">Lamb Madras</span><span class="leader"></span><span class="price">10.95</span></p>
        <p class="desc">The popular dish of madras cooked with plum tomato , degi chilli , coconut and finished with hint of lemon juice.</p>
      </div>
      <div class="item">
        <p class="item-line"><span class="name">Palak Gosht</span><span class="codes">3,</span><span class="veg">V</span><span class="leader"></span><span class="price">10.95</span></p>
        <p class="desc">Pan-fried lamb pieces cooked with spinach, fresh herbs, ginger and touch of cream</p>
      </div>
      <div class="item">
        <p class="item-line"><span class="name">Lamb Roganjosh</span><span class="leader"></span><span class="price">10.95</span></p>
        <p class="desc">Slow cooked tender lamb in kashmiri style with fresh herbs and Himalayan spices.</p>
      </div>
      <div class="item">
        <p class="item-line"><span class="name">Lamb Kohlapuri</span><span class="codes">3,4,5</span><span class="leader"></span><span class="price">10.95</span></p>
        <p class="desc">Lamb dish from South Coast of India Flavoured with yoghurt, nuts and coconut.</p>
      </div>
    </div>
  </section>

  <section class="col col-3">
    <div class="block" style="top:2px">
      <div class="item">
        <p class="item-line"><span class="name">Lamb Jalfrezi</span><span class="codes">3,5</span><span class="leader"></span><span class="price">10.95</span></p>
        <p class="desc">Lamb, tossed with cubes of onions, peppers flavored with crushed coriander seeds and dry fenugreek with hint of cream.</p>
      </div>
      <div class="item">
        <p class="item-line"><span class="name">Gosht Biryani</span><span class="codes">3,5</span><span class="veg">V</span><span class="leader"></span><span class="price">11.00</span></p>
        <p class="desc">Aged rice cooked with tender lamb brown onions, home made masala and accompanied with curry sauce.</p>
      </div>
    </div>

    <h2 class="section-title" style="top:182px">Prawn Dishes</h2>
    <div class="block" style="top:230px">
      <div class="item">
        <p class="item-line"><span class="name">Prawn Masala</span><span class="codes">3</span><span class="leader"></span><span class="price">11.95</span></p>
        <p class="desc">Prawns in a smooth creamy sauce flavoured with kasoori methi &amp; tandoori spices.</p>
      </div>
      <div class="item">
        <p class="item-line"><span class="name">Prawn Karahi</span><span class="leader"></span><span class="price">11.95</span></p>
        <p class="desc">Prawns cooked with peppers, spring onion, Caramelised onion ,tomatoes &amp; whole spices</p>
      </div>
      <div class="item">
        <p class="item-line"><span class="name">Goan Prawn Curry</span><span class="codes">3,4,5</span><span class="leader"></span><span class="price">11.95</span></p>
        <p class="desc">Fisherman`s favourite prawn curry aromatic with coconut , mustard , nuts ,curryleaves and spices from goa's costal area.</p>
      </div>
      <div class="item">
        <p class="item-line"><span class="name">Prawn Bhuna</span><span class="codes">LF</span><span class="leader"></span><span class="price">11.95</span></p>
        <p class="desc">Prawns cooked in onions &amp; tomato with black pepper to bought together the kick of spices</p>
      </div>
      <div class="item">
        <p class="item-line"><span class="name">Prawn Biryani</span><span class="codes">3,6</span><span class="veg">V</span><span class="leader"></span><span class="price">11.95</span></p>
        <p class="desc">Pan fried prawn cooked with egg, green peas &amp; onion served with curry sauce.</p>
      </div>
    </div>

    <h2 class="section-title" style="top:617px">Vegetarian Dishes</h2>
    <div class="block" style="top:663px">
      <div class="item">
        <p class="item-line"><span class="name">Shahi Paneer</span><span class="leader"></span><span class="price">8.95</span></p>
        <p class="desc">Indian cheese in semi-dry sauce.</p>
      </div>
      <div class="item">
        <p class="item-line"><span class="name">Subs Maloni Mild</span><span class="leader"></span><span class="price">8.95</span></p>
        <p class="desc">Stir fried vegetables with ground spices.</p>
      </div>
      <div class="item">
        <p class="item-line"><span class="name">Dum Wale Aloo</span><span class="codes">3</span><span class="leader"></span><span class="price">8.95</span></p>
        <p class="desc">Potatoes cooked with ginger, garlic, onions, yoghurt,&amp; curry leave with cumin Flavored.</p>
      </div>
    </div>
  </section>

  <section class="col col-4">
    <div class="block" style="top:2px">
      <div class="item">
        <p class="item-line"><span class="name">Karahi Paneer</span><span class="codes">3</span><span class="leader"></span><span class="price">8.95</span></p>
        <p class="desc">Colorful curry is prepared using homemade Indian cheese (paneer)</p>
      </div>
      <div class="item">
        <p class="item-line"><span class="name">Saag Paneer</span><span class="codes">3,</span><span class="veg">V</span><span class="leader"></span><span class="price">8.95</span></p>
        <p class="desc">Pan fried cottage cheese &amp; spinach with kasoori methi &amp;fresh coriander</p>
      </div>
      <div class="item">
        <p class="item-line"><span class="name">Sambhar Vegetable Curry</span><span class="codes">4,</span><span class="veg">V</span><span class="veg mild">V</span></p>
        <p class="item-line"><span class="leader"></span><span class="price">8.95</span></p>
        <p class="desc">Vegetable curry cooked with lentil, curry leaves, and mustard seeds</p>
      </div>
      <div class="item">
        <p class="item-line"><span class="name">Vegetable Biryani</span><span class="codes">3,5,</span><span class="veg">V</span><span class="veg mild">V</span><span class="leader"></span><span class="price">8.95</span></p>
        <p class="desc">Basmati Rice cooked with vegetables, fresh herbs, spices &amp; fried golden onion. Comes with curry sauce.</p>
      </div>
    </div>

    <h2 class="section-title" style="top:282px">Nan Bread &amp; Side Orders</h2>
    <p class="note block" style="top:328px">All naan bread contains 2,3,6</p>
    <ul class="side-list block" style="top:364px">
      <li><span class="name">Naan</span><span class="leader"></span><span class="price">2.20</span></li>
      <li><span class="name">Garlic Naan</span><span class="leader"></span><span class="price">2.50</span></li>
      <li><span class="name">Garlic Chilli Naan</span><span class="leader"></span><span class="price">3.00</span></li>
      <li><span class="name">Peshwari Naan</span><span class="codes">5</span><span class="leader"></span><span class="price">3.00</span></li>
      <li><span class="name">Keema Naan</span><span class="leader"></span><span class="price">3.00</span></li>
      <li><span class="name">Coriande Naan</span><span class="leader"></span><span class="price">2.50</span></li>
      <li><span class="name">Chilli Cheese Naan</span><span class="codes">3</span><span class="leader"></span><span class="price">3.00</span></li>
      <li><span class="name">G.O.C</span><span class="leader"></span><span class="price">3.00</span></li>
      <li><span class="name">Boiled Basmati</span><span class="leader"></span><span class="price">2.00</span></li>
      <li><span class="name">Pilau Rice</span><span class="leader"></span><span class="price">2.00</span></li>
      <li><span class="name">Lemon Rice</span><span class="codes">4</span><span class="leader"></span><span class="price">3.00</span></li>
      <li><span class="name">Poppodum(2)</span><span class="leader"></span><span class="price">2.50</span></li>
      <li><span class="name">Riata</span><span class="codes">3</span><span class="leader"></span><span class="price">2.50</span></li>
    </ul>

    <div class="photos">
      <div class="photo"><svg role="img" aria-label="Photo of a curry dish in a bowl"><rect width="100%" height="100%" fill="var(--tile-1)"/></svg></div>
      <div class="photo"><svg role="img" aria-label="Photo of fried chicken pieces"><rect width="100%" height="100%" fill="var(--tile-2)"/></svg></div>
      <div class="photo"><svg role="img" aria-label="Photo of naan bread"><rect width="100%" height="100%" fill="var(--tile-3)"/></svg></div>
      <div class="photo"><svg role="img" aria-label="Photo of basmati rice"><rect width="100%" height="100%" fill="#efe6cf"/></svg></div>
      <div class="photo"><svg role="img" aria-label="Photo of a tandoori platter"><rect width="100%" height="100%" fill="var(--tile-2)"/></svg></div>
      <div class="photo"><svg role="img" aria-label="Photo of a vegetable curry"><rect width="100%" height="100%" fill="var(--tile-1)"/></svg></div>
    </div>
  </section>

</main>
</body>
</html>
```